Online Marketing Agency Website

We are an online marketing agency that specializes in search marketing (SEM) for businesses of all sizes. Our core services include local search marketing, seo, paid search, paid social, graphic design, video production/editing and website design. We have an existing website that we launched a number of years ago but it's very outdated and we're currently too busy to design a new version.

Target Market(s)

Any business that needs online marketing services with an emphasis on search marketing.

Industry/Entity Type

Ad Agency

Number of Pages Required

4 page

Font styles to use
Sans Serif

Requirements
Must have
• Home page, interior page, blog page, contact us page.
Look and feel should be modern and clean and easy to navigate.
Sections for call outs for specific services: Business Marketing Strategy, Content Creation and Marketing, Graphic & Publication Design, Pay Per Click (PPC) Management, Search Engine Optimization, Social Media Management, Video Production & Editing, Website Hosting & Management, Website Design & Development
Use color from logo that was uploaded.

```html
<!DOCTYPE html>
<html lang="en">
<head>
<meta charset="utf-8">
<title>Lift Signal — Online Marketing Agency</title>
<link href="https://fonts.googleapis.com/css2?family=Montserrat:wght@700;800&family=Open+Sans:wght@400;600&family=Ubuntu:wght@400;500;700&display=swap" rel="stylesheet">
<style>
  :root {
    --orange: #fe4502;
    --navy: #0d3a4f;
    --cyan: #8fe6ef;
    --grey-bg: #f0f0f0;
    --line: #c9cfd3;
    --text: #24495c;
    --white: #ffffff;
  }
  * { margin: 0; padding: 0; box-sizing: border-box; }
  html, body { width: 1200px; height: 3605px; overflow: hidden; background: var(--white); }
  body { position: relative; font-family: "Open Sans", sans-serif; color: var(--navy); }
  .abs { position: absolute; }

  /* hero */
  .hero-photo { left: 280px; top: 0; width: 920px; height: 714px;
    background: linear-gradient(90deg, #fff 0%, rgba(255,255,255,.6) 22%, rgba(255,255,255,0) 45%),
                linear-gradient(160deg, #efe6da 0%, #d7c2a4 35%, #8e7157 60%, #4f4a47 80%, #cfc2b4 100%); }

  /* header */
  .brand { left: 112px; top: 82px; font-family: "Ubuntu", sans-serif; font-weight: 500; font-size: 16px; color: var(--navy); letter-spacing: .5px; display: flex; align-items: center; gap: 8px; }
  .brand-dot { width: 12px; height: 12px; background: var(--orange); border-radius: 50%; }
  .nav { top: 52px; font-size: 14px; color: var(--navy); letter-spacing: .3px; }

  .hero-title { left: 110px; top: 250px; font-family: "Montserrat", sans-serif; font-weight: 800; font-size: 58px; line-height: 70px; color: var(--navy); letter-spacing: -.5px; }
  .hero-lead { left: 110px; top: 472px; width: 480px; font-size: 18px; line-height: 32px; color: var(--text); }

  /* callout band */
  .band { left: 0; top: 714px; width: 1200px; height: 166px; background: var(--orange); }
  .band-text { left: 0; top: 757px; width: 1200px; text-align: center; font-family: "Montserrat", sans-serif; font-weight: 700; font-size: 25px; line-height: 41px; color: var(--white); }
  .quote { top: 745px; font-family: "Montserrat", sans-serif; font-weight: 800; font-size: 110px; line-height: 110px; color: #ff7a4a; }

  /* services */
  .section-title { width: 1200px; left: 0; text-align: center; font-family: "Montserrat", sans-serif; font-weight: 800; font-size: 40px; line-height: 50px; color: var(--navy); }
  .service-card { top: 1158px; width: 308px; height: 334px; }
  .service-card.is-active { background: var(--white); box-shadow: 0 4px 18px rgba(0,0,0,.08); }
  .service-visual { position: absolute; top: 55px; left: 50%; transform: translateX(-50%); width: 180px; height: 140px; border-radius: 10px; }
  .service-name { position: absolute; top: 250px; width: 100%; text-align: center; font-family: "Ubuntu", sans-serif; font-size: 32px; color: var(--navy); }

  /* blog */
  .blog-bg { left: 0; top: 1672px; width: 1200px; height: 1002px; background: var(--grey-bg); }
  .post { top: 1885px; }
  .post-photo { width: 100%; height: 307px; border-radius: 3px; }
  .post-title { margin-top: 40px; font-family: "Ubuntu", sans-serif; font-weight: 700; font-size: 21px; line-height: 25px; color: var(--navy); }
  .post-meta { margin-top: 20px; font-size: 15px; color: var(--text); }
  .post-body { margin-top: 18px; font-size: 14.2px; line-height: 23px; color: var(--text); }
  .post-body a { color: var(--orange); text-decoration: none; margin-left: 6px; }
  .more-btn { left: 511px; top: 2525px; width: 176px; height: 45px; border: 1px solid #7d8a91; border-radius: 4px; font-size: 16px; color: var(--navy); display: flex; align-items: center; justify-content: center; }

  /* contact */
  .info-head { left: 110px; font-family: "Ubuntu", sans-serif; font-weight: 500; font-size: 22px; color: var(--navy); }
  .info-line { left: 110px; font-size: 16px; line-height: 32px; color: var(--text); }
  .field { border: 1px solid var(--line); border-radius: 3px; background: var(--white); font-size: 12px; color: #8a979e; padding: 15px 18px; }
  .captcha { left: 425px; top: 3254px; width: 266px; height: 66px; border: 1px solid #d3d3d3; border-radius: 3px; background: #f9f9f9; box-shadow: 0 0 3px rgba(0,0,0,.08); display: flex; align-items: center; padding-left: 12px; gap: 12px; font-size: 12px; color: #333; }
  .captcha-box { width: 24px; height: 24px; border: 2px solid #c1c1c1; border-radius: 2px; background: #fff; }
  .captcha-mark { position: absolute; right: 18px; top: 18px; width: 28px; height: 28px; border-radius: 50%; background: #c7d3e6; }
  .send-btn { left: 425px; top: 3345px; width: 132px; height: 43px; background: var(--orange); border-radius: 3px; color: var(--white); font-family: "Ubuntu", sans-serif; font-weight: 700; font-size: 14px; display: flex; align-items: center; justify-content: center; }

  /* footer */
  .footer { left: 0; top: 3518px; width: 1200px; height: 87px; background: var(--orange); }
  .footer-text { left: 110px; top: 3553px; font-size: 16px; color: var(--white); }
</style>
</head>
<body>

  <!-- hero -->
  <div class="abs hero-photo" role="img" aria-label="Photo of a smiling team gathered around a laptop in a bright office"></div>

  <!-- header -->
  <div class="abs brand"><span class="brand-dot"></span>LIFT SIGNAL</div>
  <div class="abs nav" style="left:662px">HOME</div>
  <div class="abs nav" style="left:757px">SERVICES</div>
  <div class="abs nav" style="left:883px">BLOG</div>
  <div class="abs nav" style="left:978px">CONTACT</div>

  <h1 class="abs hero-title">A FULL-SERVICE<br>ONLINE MARKETING<br>AGENCY</h1>
  <p class="abs hero-lead">We can handle any element of your online marketing so you can get back to doing what you do best growing your business.</p>

  <!-- callout band -->
  <div class="abs band"></div>
  <div class="abs quote" style="left:160px">“</div>
  <div class="abs quote" style="left:990px">”</div>
  <p class="abs band-text">ALL OF OUR SERVICES ARE OFFERED ON AN<br>‘A LA CARTE’ BASIS</p>

  <!-- services -->
  <h2 class="abs section-title" style="top:998px">WHAT CAN WE HELP TO<br>GROWING YOUR BUSINESS</h2>

  <div class="abs service-card is-active" style="left:120px">
    <div class="service-visual" role="img" aria-label="Strategy illustration" style="background:linear-gradient(135deg,#ffd9c9,#d9f7fa)"></div>
    <div class="service-name">Strategy</div>
  </div>

  <div class="abs service-card" style="left:446px">
    <div class="service-visual" role="img" aria-label="Content illustration" style="background:linear-gradient(135deg,#ffd9c9,#d9f7fa)"></div>
    <div class="service-name">Content</div>
  </div>

  <div class="abs service-card" style="left:775px">
    <div class="service-visual" role="img" aria-label="Optimization illustration" style="background:linear-gradient(135deg,#ffd9c9,#d9f7fa)"></div>
    <div class="service-name">Optimization</div>
  </div>

  <!-- blog -->
  <div class="abs blog-bg"></div>
  <h2 class="abs section-title" style="top:1778px">BLOG</h2>

  <article class="abs post" style="left:117px;width:308px">
    <div class="post-photo" role="img" aria-label="Photo of two colleagues talking in an open-plan office" style="background:linear-gradient(135deg,#c9cdd2,#5a6f8c 55%,#2d3440)"></div>
    <h3 class="post-title">Lorem ipsum dolor sit amet, consectetur adipiscing elit.</h3>
    <p class="post-meta">Maren Holt &nbsp;|&nbsp; Apr 22, 2020</p>
    <p class="post-body">Pellentesque at tincidunt lorem, sollicitudin eleifend ante. Nunc vestibulum facilisis leo. Mauris iaculis suscipit ligula, nec luctus ligula pulvinar in. Sed eget condimentum quam.<a href="#">Read more..</a></p>
  </article>

  <article class="abs post" style="left:443px;width:309px">
    <div class="post-photo" role="img" aria-label="Photo of a laptop and monitor showing code on a wooden desk" style="background:linear-gradient(160deg,#b9bfc4,#4a4f55 50%,#8a6c4e)"></div>
    <h3 class="post-title">Lorem ipsum dolor sit amet, consectetur adipiscing elit.</h3>
    <p class="post-meta">Maren Holt &nbsp;|&nbsp; Apr 22, 2020</p>
    <p class="post-body">Pellentesque at tincidunt lorem, sollicitudin eleifend ante. Nunc vestibulum facilisis leo. Mauris iaculis suscipit ligula, nec luctus ligula pulvinar in. Sed eget condimentum quam.<a href="#">Read more..</a></p>
  </article>

  <article class="abs post" style="left:768px;width:316px">
    <div class="post-photo" role="img" aria-label="Photo of a bright open office with desks and large windows" style="background:linear-gradient(180deg,#e7e1d8,#b79f85 45%,#4b4e54)"></div>
    <h3 class="post-title">Lorem ipsum dolor sit amet, consectetur adipiscing elit.</h3>
    <p class="post-meta">Maren Holt &nbsp;|&nbsp; Apr 22, 2020</p>
    <p class="post-body">Pellentesque at tincidunt lorem, sollicitudin eleifend ante. Nunc vestibulum facilisis leo. Mauris iaculis suscipit ligula, nec luctus ligula pulvinar in. Sed eget condimentum quam.<a href="#">Read more..</a></p>
  </article>

  <div class="abs more-btn">more articles</div>

  <!-- contact -->
  <h2 class="abs section-title" style="top:2770px;left:-26px">GET IN TOUCH</h2>

  <div class="abs info-head" style="top:2856px">Lift Signal</div>
  <div class="abs info-line" style="top:2892px">Harbour Street 12, Riverton<br>Northland</div>
  <div class="abs info-head" style="top:2998px">Office Hours</div>
  <div class="abs info-line" style="top:3030px">Monday - Friday<br>08.00 am - 16.00 pm</div>
  <div class="abs info-head" style="top:3128px">Email Support</div>
  <div class="abs info-line" style="top:3160px">support.liftsignal@example.com</div>

  <div class="abs field" style="left:425px;top:2858px;width:325px;height:44px">Name*</div>
  <div class="abs field" style="left:768px;top:2858px;width:325px;height:44px">Company*</div>
  <div class="abs field" style="left:425px;top:2929px;width:325px;height:44px">Email*</div>
  <div class="abs field" style="left:768px;top:2929px;width:325px;height:44px">Services</div>
  <div class="abs field" style="left:425px;top:2999px;width:668px;height:44px">Subject*</div>
  <div class="abs field" style="left:425px;top:3069px;width:668px;height:159px">Messages*</div>

  <div class="abs captcha"><span class="captcha-box"></span>I'm not a robot<span class="captcha-mark"></span></div>
  <div class="abs send-btn">SEND!</div>

  <!-- footer -->
  <div class="abs footer"></div>
  <div class="abs footer-text">Lift Signal Copyright © 2020</div>

</body>
</html>
```